Business card for new consulting business - Brenvale Holdings Pty Ltd.

Consulting in the areas of Brenvale Holdings Pty Ltd, Safety and Community Relations in the resources (mining) industries. The consultant (me) will work both within Australia and overseas jurisdictions such as South East Asia, Africa , South America etc, often working with third world indigenous communities. The design should suggest a high level of social and environmental responsibility.

```html
<!DOCTYPE html>
<html lang="en">
<head>
<meta charset="utf-8">
<title>Brenvale Holdings Pty Ltd – Business Card</title>
<link rel="stylesheet" href="https://fonts.googleapis.com/css2?family=Quicksand:wght@500;600&family=Open+Sans:wght@400;600&family=Arimo:wght@400&display=swap">
<style>
  :root {
    --page-bg: #e9eaea;
    --card-bg: #ffffff;
    --brand-blue: #2f7df0;
    --brand-green: #1f9a1c;
    --ink: #1b1b1b;
    --ink-soft: #3a3a3a;
    --tab-blue: #4a8ff0;
  }
  * { margin: 0; padding: 0; box-sizing: border-box; }
  html, body {
    width: 1200px; height: 1200px; overflow: hidden;
    background: var(--page-bg);
  }
  .canvas { position: relative; width: 1200px; height: 1200px; }
  .card {
    position: absolute; left: 298px; width: 666px; height: 380px;
    background: var(--card-bg);
    box-shadow: 0 1px 3px rgba(0,0,0,0.12);
    overflow: hidden;
  }
  .card--front { top: 198px; }
  .card--back { top: 637px; }

  .brand { position: absolute; text-align: center; font-family: "Quicksand", sans-serif; }
  .brand__dot { display: block; margin: 0 auto; border-radius: 50%; background: var(--brand-green); }
  .brand__name { color: var(--brand-blue); font-weight: 600; white-space: nowrap; }
  .brand__line { color: var(--ink); font-weight: 500; white-space: nowrap; }

  .card--front .brand { left: 320px; width: 340px; top: 200px; }
  .card--front .brand__dot { width: 64px; height: 64px; margin-bottom: 34px; }
  .card--front .brand__name { font-size: 24px; line-height: 1.1; }
  .card--front .brand__line { font-size: 17px; margin-top: 6px; }

  .card--back .brand { left: 45px; width: 200px; top: 60px; }
  .card--back .brand__dot { width: 40px; height: 40px; margin-bottom: 30px; }
  .card--back .brand__name { font-size: 15px; line-height: 1.1; }
  .card--back .brand__line { font-size: 11px; margin-top: 4px; }

  .person { position: absolute; right: 62px; top: 78px; text-align: right; font-family: "Open Sans", sans-serif; }
  .person__name { color: var(--brand-blue); font-size: 26px; font-weight: 600; line-height: 1; }
  .person__role { color: var(--ink-soft); font-size: 16px; margin-top: 4px; }
  .person-tab {
    position: absolute; right: 0; top: 82px; width: 48px; height: 36px;
    background: var(--tab-blue); border-radius: 4px 0 0 4px;
    display: flex; align-items: center; justify-content: center;
  }

  .contact { position: absolute; left: 35px; top: 264px; list-style: none; font-family: "Arimo", sans-serif; }
  .contact__item { display: flex; align-items: center; height: 25px; font-size: 16.5px; color: var(--ink); }
  .contact__icon { width: 18px; height: 18px; margin-right: 10px; flex: none; }

  .address {
    position: absolute; right: 40px; top: 300px; text-align: right; font-style: normal;
    font-family: "Arimo", sans-serif; font-size: 15.5px; line-height: 1.25; color: var(--ink);
  }
</style>
</head>
<body>
<main class="canvas">
  <section class="card card--front">
    <div class="brand">
      <span class="brand__dot"></span>
      <div class="brand__name">Brenvale Holdings Pty Ltd</div>
      <div class="brand__line">Safety and Community Relations</div>
    </div>
  </section>

  <section class="card card--back">
    <div class="brand">
      <span class="brand__dot"></span>
      <div class="brand__name">Brenvale Holdings Pty Ltd</div>
      <div class="brand__line">Safety and Community Relations</div>
    </div>

    <div class="person">
      <div class="person__name">Daniel Harwood</div>
      <div class="person__role">President</div>
    </div>
    <div class="person-tab">
      <svg width="26" height="28" viewBox="0 0 26 28" aria-hidden="true">
        <rect x="2" y="2" width="22" height="24" rx="3" fill="none" stroke="#fff" stroke-width="2"/>
        <circle cx="13" cy="11" r="4.5" fill="#fff"/>
        <path d="M5 24c1-5 4.5-7 8-7s7 2 8 7z" fill="#fff"/>
      </svg>
    </div>

    <ul class="contact">
      <li class="contact__item">
        <svg class="contact__icon" viewBox="0 0 24 24" aria-hidden="true"><path fill="var(--brand-blue)" d="M6.6 10.8a15 15 0 0 0 6.6 6.6l2.2-2.2c.3-.3.7-.4 1-.2 1.1.4 2.3.6 3.6.6.6 0 1 .4 1 1V20c0 .6-.4 1-1 1A17 17 0 0 1 3 4c0-.6.4-1 1-1h3.5c.6 0 1 .4 1 1 0 1.3.2 2.5.6 3.6.1.3 0 .7-.2 1z"/></svg>
        000 418 2760
      </li>
      <li class="contact__item">
        <svg class="contact__icon" viewBox="0 0 24 24" aria-hidden="true"><circle cx="12" cy="12" r="4" fill="none" stroke="var(--brand-blue)" stroke-width="2.4"/><path d="M16 8v5.5c0 2 3.5 2 3.5-1.5A7.5 7.5 0 1 0 15 19" fill="none" stroke="var(--brand-blue)" stroke-width="2.4" stroke-linecap="round"/></svg>
        info@brenvaleholdings.com
      </li>
      <li class="contact__item">
        <svg class="contact__icon" viewBox="0 0 24 24" aria-hidden="true"><g fill="none" stroke="var(--brand-blue)" stroke-width="1.4"><circle cx="12" cy="12" r="10"/><ellipse cx="12" cy="12" rx="4.5" ry="10"/><path d="M2 12h20M4 7h16M4 17h16M12 2v20"/></g></svg>
        brenvaleholdings.com
      </li>
    </ul>

    <address class="address">
      Your street address,<br>singapure, 23
    </address>
  </section>
</main>
</body>
</html>
```